3D Printing Business coming soon page

Hi we are looking for a one page "coming soon" website for our business. The business is called "Solevia Labs" and it is a new solution which 3D Prints Orthotics (Insoles).

The design should include our logo, an improved version of our promotional image (attached), a web form for capturing interest from people, a countdown timer and some text.

Follow the colour scheme which is shown in our logo along with our other colours - Orange (RGB#ff8300) and Light Green (RGB#30f20a)
Updates

Industry/Entity Type

Business

Font styles to use
Sans Serif

Requirements
Must have
• Logo (Attached)
Improved version of Promotional Image
Web Form design for capturing Name, EMail Address and Comments along with a Turin test
Countdown Timer
Text - "Solevia Labs will shake up the Orthotics Industry. Foot Orthosis patient-ready in hours for a fraction of the price you are paying today. Welcome to the new world of 3D Printing!"

```html
<!DOCTYPE html>
<html lang="en">
<head>
<meta charset="utf-8">
<title>Solevia Labs – Coming Soon</title>
<link href="https://fonts.googleapis.com/css2?family=Roboto+Condensed:ital,wght@0,300;0,400;0,700;1,900&family=Roboto:wght@400;500&display=swap" rel="stylesheet">
<style>
:root{
  --orange:#ff8300;
  --orange-light:#ffc46a;
  --green:#30f20a;
  --body-bg:#ececec;
  --ink:#111;
  --muted:#666;
  --line:#d2d2d2;
  --blue:#1e78a8;
  --tab-blue:#29a8e0;
  --footer:#232323;
  --white:#fff;
}
*{margin:0;padding:0;box-sizing:border-box}
html,body{width:1200px;height:843px;overflow:hidden}
body{position:relative;background:var(--body-bg);font-family:"Roboto",Arial,sans-serif;color:var(--ink)}
.abs{position:absolute}

/* header */
.site-header{position:absolute;left:0;top:0;width:1200px;height:102px;background:var(--orange)}
.header-edge{position:absolute;left:0;top:100px;width:1200px;height:6px}
.brand{position:absolute;left:262px;top:20px;display:flex;align-items:center;gap:12px;font-family:"Roboto Condensed",sans-serif;font-weight:400;font-size:52px;line-height:1;color:var(--white);letter-spacing:-1px}
.brand-dot{width:44px;height:44px;border-radius:50%;background:var(--white)}
.call-tab{position:absolute;height:13px;background:var(--tab-blue);color:var(--white);font-size:11px;line-height:13px;padding-left:22px;clip-path:polygon(8px 0,100% 0,100% 100%,0 100%)}
.phone{position:absolute;color:var(--white);font-size:28px;line-height:1;letter-spacing:.5px}

/* welcome band */
.welcome-band{position:absolute;left:0;top:106px;width:1200px;height:52px;background:var(--green);text-align:center;font-family:"Roboto Condensed",sans-serif;font-weight:300;font-size:29px;line-height:54px;color:var(--ink)}
.welcome-band strong{font-weight:700;font-size:32px}

/* steps */
.step-label{position:absolute;width:120px;text-align:center;font-size:9px;color:#aaa;top:185px}
.step-photo{position:absolute;top:204px;width:112px;height:112px;border-radius:50%;border:4px solid var(--orange)}
.step-title{position:absolute;top:328px;width:200px;text-align:center;font-family:"Roboto Condensed",sans-serif;font-size:18px;color:var(--ink)}
.step-arrow{position:absolute;top:241px}
.rule{position:absolute;height:1px;background:var(--line)}

/* form */
.signup{position:absolute;left:248px;top:375px;width:242px;height:378px;border-radius:4px;border:1px solid #e88a1a;background:linear-gradient(#ffb860,#ffa23a 60%,#ff9420)}
.signup-title{position:absolute;left:10px;top:9px;width:222px;height:48px;border-radius:8px 8px 0 0;background:linear-gradient(#ffe6bd,#ffcf84);font-family:"Roboto Condensed",sans-serif;font-style:italic;font-weight:900;font-size:26px;line-height:50px;text-align:center;color:#1a1a1a}
.field-label{position:absolute;right:160px;font-size:10px;color:#222}
.field{position:absolute;left:92px;width:136px;background:var(--white);border:1px solid #f0d0a0}
.captcha{position:absolute;left:92px;top:232px;width:136px;height:26px;background:var(--white);font-family:Georgia,serif;font-style:italic;font-size:15px;line-height:26px;text-align:center;color:#222;letter-spacing:-.5px}
.captcha-hint{position:absolute;left:93px;top:264px;font-size:10px;color:#222}
.captcha-tools{position:absolute;right:0;top:0;width:14px;height:100%;border-left:1px solid #ddd}
.captcha-tools i{display:block;width:5px;height:5px;border-radius:50%;background:#c33;margin:4px auto 0}
.submit{position:absolute;left:51px;top:324px;width:148px;height:41px;border-radius:8px;border:1px solid #e8901c;background:linear-gradient(#ffd58a,#ffad3c 55%,#ff9a18);font-family:"Roboto Condensed",sans-serif;font-style:italic;font-weight:900;font-size:21px;line-height:40px;text-align:center;color:#1a1a1a}

/* intro */
.intro-name{position:absolute;left:495px;top:388px;width:480px;text-align:center;font-family:"Roboto Condensed",sans-serif;font-weight:400;font-size:46px;line-height:1;color:var(--blue)}
.point{position:absolute;left:540px;display:flex;align-items:center;gap:18px}
.point-mark{flex:none;width:34px;height:34px;border-radius:50%;background:#f7a51c}
.point-text{font-family:"Roboto Condensed",sans-serif;font-size:17px;line-height:23px;color:var(--muted)}

/* footer */
.site-footer{position:absolute;left:0;top:764px;width:1200px;height:79px;background:var(--footer)}
.countdown{position:absolute;left:822px;top:15px;display:flex;gap:3px;align-items:flex-start}
.unit{width:36px;text-align:center}
.digits{height:34px;background:linear-gradient(#3a3a3a,#111);border:1px solid #444;border-radius:2px;color:#ddd;font-family:"Roboto Condensed",sans-serif;font-size:27px;line-height:34px}
.unit-name{font-size:7px;color:#ccc;margin-top:4px}
.colon{color:#ddd;font-size:20px;line-height:34px;width:2px}
</style>
</head>
<body>

<header class="site-header">
  <div class="brand"><span class="brand-dot"></span>Solevia Labs</div>
  <div class="call-tab" style="left:862px;top:32px;width:115px">Call us to Join</div>
  <div class="phone" style="left:780px;top:48px">+888 410 2265</div>
</header>
<svg class="header-edge" viewBox="0 0 1200 6" preserveAspectRatio="none" aria-hidden="true">
  <defs><pattern id="teeth" width="6" height="6" patternUnits="userSpaceOnUse"><path d="M0 0H6L3 6Z" fill="#ff8300"/></pattern></defs>
  <rect width="1200" height="6" fill="url(#teeth)"/>
</svg>

<div class="welcome-band">WELCOME TO THE NEW WORLD OF <strong>3D PRINTING!</strong></div>

<section class="steps">
  <div class="step-label" style="left:254px">STEP 1</div>
  <div class="step-label" style="left:444px">STEP 2</div>
  <div class="step-label" style="left:651px">STEP 3</div>
  <div class="step-label" style="left:842px">STEP 4</div>

  <div class="step-photo" style="left:258px;background:radial-gradient(circle,#5a6a86,#2a2a2e)" role="img" aria-label="Laptop showing a foot pressure scan"></div>
  <div class="step-photo" style="left:449px;background:radial-gradient(circle,#e7d8c4,#f4f1ec)" role="img" aria-label="Hand holding a designed orthotic insole"></div>
  <div class="step-photo" style="left:655px;background:radial-gradient(circle,#c9c9cc,#9a2e44)" role="img" aria-label="Desktop 3D printer"></div>
  <div class="step-photo" style="left:846px;background:radial-gradient(circle,#cbb08a,#1c1c1c)" role="img" aria-label="Insole being fitted into a shoe"></div>

  <svg class="step-arrow" style="left:378px" width="66" height="36" viewBox="0 0 66 36" aria-hidden="true"><path d="M0 9H46V0L66 18 46 36V27H0Z" fill="#000"/></svg>
  <svg class="step-arrow" style="left:576px" width="66" height="36" viewBox="0 0 66 36" aria-hidden="true"><path d="M0 9H46V0L66 18 46 36V27H0Z" fill="#000"/></svg>
  <svg class="step-arrow" style="left:774px" width="66" height="36" viewBox="0 0 66 36" aria-hidden="true"><path d="M0 9H46V0L66 18 46 36V27H0Z" fill="#000"/></svg>

  <div class="step-title" style="left:216px">SCAN THE FOOT</div>
  <div class="step-title" style="left:414px">DESIGN THE ORTHOTIC</div>
  <div class="step-title" style="left:611px">3D PRINT IT</div>
  <div class="step-title" style="left:803px">FIT IT</div>
</section>

<div class="rule" style="left:240px;top:365px;width:735px"></div>

<form class="signup">
  <div class="signup-title">Get Started Now !</div>
  <label class="field-label" style="top:84px">First Name</label>
  <div class="field" style="top:83px;height:15px"></div>
  <label class="field-label" style="top:108px">Last Name</label>
  <div class="field" style="top:106px;height:15px"></div>
  <label class="field-label" style="top:132px">E-mail Address</label>
  <div class="field" style="top:131px;height:15px"></div>
  <label class="field-label" style="top:157px">Message</label>
  <div class="field" style="top:156px;height:68px"></div>
  <div class="captcha">poration submits</div>
  <div class="captcha-hint">Type the above words:</div>
  <div class="field" style="top:278px;height:28px"><div class="captcha-tools"><i></i><i></i><i></i></div></div>
  <div class="submit">SUBMIT</div>
</form>

<section class="intro">
  <div class="intro-name">Solevia Labs</div>
  <div class="rule" style="left:495px;top:450px;width:480px"></div>
  <div class="point" style="top:485px"><span class="point-mark"></span><p class="point-text">Solevia Labs will shake up the Orthotics Industry.</p></div>
  <div class="point" style="top:546px"><span class="point-mark"></span><p class="point-text">Foot Orthosis patient-ready in hours for a fraction of<br>the price you are paying today.</p></div>
  <div class="point" style="top:608px"><span class="point-mark"></span><p class="point-text">Welcome to the new world of 3D Printing!</p></div>
  <div class="rule" style="left:495px;top:662px;width:480px"></div>
</section>
<svg class="abs" style="left:540px;top:485px" width="34" height="160" viewBox="0 0 34 160" aria-hidden="true">
  <g fill="none" stroke="#fff" stroke-width="1.5"><path d="M13 17H21M18 14L21 17 18 20"/><path d="M13 83H21M18 80L21 83 18 86"/><path d="M13 140H21M18 137L21 140 18 143"/></g>
</svg>

<footer class="site-footer">
  <div class="call-tab" style="left:240px;top:21px;width:115px;padding-left:6px;clip-path:polygon(0 0,calc(100% - 8px) 0,100% 100%,0 100%)">Call us to Join</div>
  <div class="phone" style="left:240px;top:35px">+888 410 2265</div>
  <div class="countdown">
    <div class="unit"><div class="digits">01</div><div class="unit-name">DAYS</div></div>
    <span class="colon">:</span>
    <div class="unit"><div class="digits">06</div><div class="unit-name">HRS</div></div>
    <span class="colon">:</span>
    <div class="unit"><div class="digits">35</div><div class="unit-name">MINS</div></div>
    <span class="colon">:</span>
    <div class="unit"><div class="digits">48</div><div class="unit-name">SECS</div></div>
  </div>
</footer>

</body>
</html>
```